Buchcover-Design für psychologischen Ratgeber Morgens voller Mut!
Zielgruppe
Veröffentlichung psychologischer Ratgeber. Zielgruppe sind Erwachsene.
Aufgabenstellung
keine besondere Vorgaben, ein eyecatching-Cover wäre super. Der Titel des Buches lautet: Morgens voller Mut! Der Untertitel lautet: Heitere Seelenkunde für stille Kraft und Zuversicht
Autoren: Dr. Hanna Wiesmoor-Kalbach, Dr. Lukas Kalbach
Vielleicht macht es Sinn, einen Button mit: 199 Praxistipps auf dem Cover anzuführen.
Das Buch wird als Softcover und Ebook auf lesewelt veröffentlicht. Das Format ist 6 mal 9 Zoll und hat 425 Seiten.

```html
<!DOCTYPE html>
<html lang="de">
<head>
<meta charset="utf-8">
<title>Morgens voller Mut! – Buchcover</title>
<link rel="stylesheet" href="https://fonts.googleapis.com/css2?family=Comfortaa:wght@500&family=Fira+Sans+Extra+Condensed:wght@600;700&family=Fira+Sans+Condensed:wght@700&display=swap">
<style>
  :root {
    --ink-red: #d42335;
    --ink-navy: #16284a;
    --cream: #f1ead2;
    --band-top: #f5d00f;
    --band-mid: #f3b412;
    --band-bottom: #f07510;
    --paper-light: #f3f4f6;
    --paper-shade: #e2e4e8;
    --paper-blush: #f2d6d9;
    --black: #000000;
    --white: #ffffff;
  }
  * { margin: 0; padding: 0; box-sizing: border-box; }
  html, body { width: 800px; height: 1200px; overflow: hidden; background: var(--white); }
  .cover {
    position: relative;
    width: 800px;
    height: 1200px;
    overflow: hidden;
    font-family: "Fira Sans Condensed", sans-serif;
  }
  .cover-photo {
    position: absolute;
    left: 0; top: 0;
    width: 800px; height: 625px;
    background:
      radial-gradient(ellipse 260px 180px at 420px 320px, rgba(236, 120, 130, 0.28), rgba(236, 120, 130, 0) 70%),
      radial-gradient(ellipse 200px 140px at 620px 540px, rgba(236, 120, 130, 0.22), rgba(236, 120, 130, 0) 70%),
      radial-gradient(ellipse 220px 160px at 120px 320px, rgba(236, 150, 160, 0.22), rgba(236, 150, 160, 0) 70%),
      linear-gradient(145deg, var(--paper-light) 0%, var(--paper-light) 38%, var(--paper-shade) 39%, var(--paper-blush) 70%, var(--paper-shade) 100%);
  }
  .publisher {
    position: absolute;
    left: 287px; top: 0;
    width: 230px; height: 89px;
    background: var(--black);
    color: var(--white);
    display: flex; align-items: center; justify-content: center;
    font-family: "Fira Sans Condensed", sans-serif;
    font-weight: 700;
    font-size: 27px;
    padding-top: 14px;
  }
  .info-band {
    position: absolute;
    left: 0; top: 625px;
    width: 800px; height: 575px;
    background: linear-gradient(160deg, var(--band-top) 0%, var(--band-mid) 55%, var(--band-bottom) 100%);
  }
  .authors {
    position: absolute;
    left: 0; top: 658px; width: 800px;
    text-align: center;
    font-family: "Fira Sans Extra Condensed", sans-serif;
    font-weight: 700;
    font-size: 31px;
    color: var(--ink-navy);
  }
  .rule {
    position: absolute;
    height: 0;
    border-top: 1.5px dashed var(--ink-navy);
  }
  .rule-top { left: 117px; top: 700px; width: 595px; }
  .rule-bottom { left: 110px; top: 1034px; width: 585px; border-top-color: var(--cream); }
  .title {
    position: absolute;
    left: 0; top: 712px; width: 800px;
    text-align: center;
    font-family: "Comfortaa", sans-serif;
    font-weight: 500;
    font-size: 142px;
    line-height: 134px;
    letter-spacing: -2px;
    color: var(--ink-red);
  }
  .subtitle-kicker {
    position: absolute;
    left: 0; top: 1050px; width: 800px;
    text-align: center;
    font-family: "Fira Sans Extra Condensed", sans-serif;
    font-weight: 700;
    font-size: 44px;
    letter-spacing: 11px;
    padding-left: 11px;
    color: var(--cream);
  }
  .subtitle-line {
    position: absolute;
    left: 0; top: 1104px; width: 800px;
    text-align: center;
    font-family: "Fira Sans Extra Condensed", sans-serif;
    font-weight: 700;
    font-size: 50px;
    color: var(--ink-navy);
  }
</style>
</head>
<body>
  <main class="cover">
    <div class="cover-photo" role="img" aria-label="Foto: Wandkalender in Nahaufnahme, jeder Tag mit einem rot gezeichneten Smiley markiert"></div>
    <div class="publisher">Verlag Morgenrot</div>

    <section class="info-band"></section>
    <p class="authors">Dr. Hanna Wiesmoor-Kalbach &amp; Dr. Lukas Kalbach</p>
    <div class="rule rule-top"></div>
    <h1 class="title">Morgens<br>voller Mut!</h1>
    <div class="rule rule-bottom"></div>
    <p class="subtitle-kicker">HEITERE SEELENKUNDE</p>
    <p class="subtitle-line">für stille Kraft &amp; Zuversicht</p>
  </main>
</body>
</html>
```